Killer Webpage Design

I currently have a self-hosted webpage through wordpress at www.vantrelmedia.com - the content is complete and I'm happy with this but I need it designed (no coding) to complete my requirements. I'm happy to take designs which are non-Wordpress if there is specific advantage in this.

My full branding logos are attached along with color files. My main aim is consistent branding across all areas (social media, business cards, emails, websites). I have the rest running but am not happy with the available default selections from Wordpress.

I would prefer to use the darker blue version of the logo as I feel this has more standout in online media, however I would appreciate submissions with both variants to help me choose.

With the homepage I will also want to see blog pages and category pages designed but this can come after I have selected a design to go with,

Sites that I like and are related to my business include the following:
http://www.plumora.com/au/accounting-software/
http://www.taskgriddle.com/home.aspx
https://brimtill.com/register
Updates

Apologies for the confusion - to clarify for designers I am looking for design only, no coding.

FYI - i have now uploaded business cards for an idea of the contemporary style of design completed so far.

Target Market(s)

small to medium business. Not systemised but looking for help and support.

Industry/Entity Type

Business

Requirements
Must have
• I'm looking for a minimalist professional page, with the ability to easily add new sections when required. I will also need a CMS to add blog posts on the go, with the same features that it currently has (comments, social logon etc)

```html
<!DOCTYPE html>
<html lang="en">
<head>
<meta charset="utf-8">
<title>Vantrel Media</title>
<link href="https://fonts.googleapis.com/css2?family=Open+Sans:wght@400;700&family=PT+Sans:wght@400;700&display=swap" rel="stylesheet">
<style>
:root{
  --teal:#13b4c4;
  --hero:#12c4d0;
  --navy:#0b2a3b;
  --ink:#777777;
  --dark:#3d3d3d;
  --panel:#f3f3f3;
  --rule:#e3e3e3;
  --white:#ffffff;
}
*{margin:0;padding:0;box-sizing:border-box}
html,body{width:905px;height:1200px;overflow:hidden;background:var(--white)}
body{position:relative;font-family:"PT Sans",sans-serif;color:var(--ink)}
.abs{position:absolute}
.site-header{left:0;top:0;width:905px;height:80px}
.brand{left:142px;top:22px;display:flex;align-items:center;gap:8px}
.brand-dot{width:34px;height:34px;border-radius:50%;background:var(--teal)}
.brand-name{font-size:23px;font-weight:700;color:var(--navy)}
.social{right:143px;top:25px;display:flex;gap:7px}
.social span{width:29px;height:29px;border-radius:50%;background:var(--navy);display:block}
.main-nav{left:0;top:80px;width:905px;height:30px;background:var(--navy);display:flex;justify-content:center;align-items:center;font-size:9px;color:var(--white);text-transform:uppercase}
.main-nav a{color:inherit;text-decoration:none}
.main-nav a.current{color:var(--teal)}
.main-nav .sep{margin:0 11px;opacity:.8}
.hero{left:0;top:110px;width:905px;height:308px;background:linear-gradient(180deg,#10bfcc,var(--hero))}
.hero-media{left:142px;top:28px;width:408px;height:238px;border-radius:6px;background:linear-gradient(180deg,#6f7a80,#3c4347)}
.dots{left:334px;top:278px;display:flex;gap:5px}
.dots span{width:10px;height:10px;border-radius:50%;background:var(--white)}
.dots span.on{background:transparent;border:2px solid var(--white)}
.hero-title{left:567px;top:80px;color:var(--white);font-family:"Open Sans",sans-serif;line-height:1}
.hero-title small{display:block;font-size:19px;font-weight:400}
.hero-title strong{display:block;font-size:26px;font-weight:700;margin-top:1px}
.hero-quote{left:568px;top:134px;width:200px;color:var(--white);font-family:"Open Sans",sans-serif;font-size:10px;line-height:14.3px;padding-left:17px}
.hero-quote .q{position:absolute;font-size:18px;font-weight:700;line-height:1}
.hero-quote .q-end{position:absolute;right:-16px;bottom:-6px;font-size:18px;font-weight:700;line-height:1}
.section-title{display:flex;align-items:center;gap:7px;color:var(--teal);font-size:13px;font-weight:700;text-transform:uppercase}
.section-title i{width:16px;height:16px;border-radius:50%;background:var(--teal);display:block}
.welcome-title{left:142px;top:446px}
.welcome-photo{left:142px;top:476px;width:157px;height:126px;background:linear-gradient(135deg,#b9b2aa,#4a4d55)}
.welcome-text{left:310px;top:472px;width:245px;font-size:9px;line-height:12.95px}
.btn-more{left:497px;top:584px;width:58px;height:20px;border-radius:3px;background:var(--teal);color:var(--white);font-size:8.6px;display:flex;align-items:center;justify-content:center}
.services-title{left:569px;top:446px}
.services{left:571px;top:469px;list-style:none;font-size:8.6px}
.services li{height:19.5px;display:flex;align-items:center;gap:6px}
.services svg{width:5px;height:8px}
.divider{left:142px;top:623px;width:620px;height:1px;background:var(--rule)}
.blog-title{left:142px;top:640px}
.post{left:142px;width:620px;height:95px;background:var(--panel);border-left:3px solid var(--teal);border-radius:3px;padding:16px 30px 0 13px}
.post h3{font-size:10px;font-weight:400;color:var(--teal);text-transform:uppercase;margin-bottom:5px}
.post p{font-size:8.6px;line-height:12.9px;color:var(--dark)}
.post a,.comment a{color:var(--teal);text-decoration:none}
.comment{left:168px;width:594px;height:60px;background:var(--panel);border-radius:3px;padding:12px 24px 0 16px;font-size:8.6px;line-height:12.9px;color:var(--ink)}
.comment .meta{display:flex;justify-content:flex-end;gap:50px;margin-top:2px}
.site-footer{left:0;top:1114px;width:905px;height:86px;background:var(--navy)}
.footer-links{left:141px;top:20px;font-size:8.6px;color:var(--teal)}
.footer-links .sep{margin:0 4px}
.copyright{left:141px;top:36px;font-size:8.6px;color:var(--teal)}
.footer-brand{right:143px;top:32px;font-size:13px;font-weight:700;color:var(--teal)}
</style>
</head>
<body>
<header class="site-header abs">
  <div class="brand abs"><span class="brand-dot"></span><span class="brand-name">Vantrel Media</span></div>
  <div class="social abs" aria-label="Social links"><span></span><span></span><span></span></div>
</header>
<nav class="main-nav abs">
  <a class="current" href="#">Software Training and Implementation</a><span class="sep">|</span>
  <a href="#">Project Management</a><span class="sep">|</span>
  <a href="#">Business Process Analysis</a><span class="sep">|</span>
  <a href="#">Blog</a><span class="sep">|</span>
  <a href="#">About Us</a><span class="sep">|</span>
  <a href="#">Contact</a>
</nav>
<section class="hero abs">
  <div class="hero-media abs" role="img" aria-label="Laptop showing three business consultants shaking hands at a meeting table"></div>
  <div class="dots abs"><span class="on"></span><span></span><span></span></div>
  <h1 class="hero-title abs"><small>SPECIALIST BUSINESS</small><strong>CONSULTANTS</strong></h1>
  <blockquote class="hero-quote abs"><span class="q" style="left:0;top:-2px">&ldquo;</span>Whatever the mind of man can conceive and believe, it can achieve. Thoughts are things! And powerful things at that, when mixed with definiteness of purpose, and burning desire, can be translated into riches<span class="q-end">&rdquo;</span></blockquote>
</section>
<h2 class="section-title welcome-title abs"><i></i>Welcome to Vantrel Media</h2>
<div class="welcome-photo abs" role="img" aria-label="Team of business people reviewing documents together"></div>
<p class="welcome-text abs">Cloud computing spending is due to account for a third of annual IT expenditure growth by the end of 2013. Every year the range of cloud software systems gets bigger, now including Plumora Accounting, Quillix Apps for Business, Jobwright Job Management Software, Corvane Deskline, Projara Project Manager and many more. Signing up for cloud software is only the first part of the process, and then it has to be implemented into your business. That's where Vantrel Media comes in. Formed</p>
<a class="btn-more abs">MORE</a>
<h2 class="section-title services-title abs"><i></i>What we do ?</h2>
<ul class="services abs">
  <li><svg viewBox="0 0 5 8"><path d="M1 1l3 3-3 3" fill="none" stroke="#13b4c4" stroke-width="1.2"/></svg>Lorem Ipsum is simply dummy</li>
  <li><svg viewBox="0 0 5 8"><path d="M1 1l3 3-3 3" fill="none" stroke="#13b4c4" stroke-width="1.2"/></svg>Text of the printing and typesetting</li>
  <li><svg viewBox="0 0 5 8"><path d="M1 1l3 3-3 3" fill="none" stroke="#13b4c4" stroke-width="1.2"/></svg>Industry. Lorem Ipsum has been</li>
  <li><svg viewBox="0 0 5 8"><path d="M1 1l3 3-3 3" fill="none" stroke="#13b4c4" stroke-width="1.2"/></svg>Industry's standard dummy text ever since</li>
  <li><svg viewBox="0 0 5 8"><path d="M1 1l3 3-3 3" fill="none" stroke="#13b4c4" stroke-width="1.2"/></svg>when an unknown printer took a galley</li>
  <li><svg viewBox="0 0 5 8"><path d="M1 1l3 3-3 3" fill="none" stroke="#13b4c4" stroke-width="1.2"/></svg>Type only five centuri</li>
  <li><svg viewBox="0 0 5 8"><path d="M1 1l3 3-3 3" fill="none" stroke="#13b4c4" stroke-width="1.2"/></svg>Lorem Ipsum is simply dummy</li>
</ul>
<div class="divider abs"></div>
<h2 class="section-title blog-title abs"><i></i>Blog Post</h2>
<article class="post abs" style="top:669px">
  <h3>Corvane Mailer to Quillix Apps</h3>
  <p>With Corvane making big strides recently to move their huge office suite into the cloud, with Corvane Deskline, this is a great time to revisit the options with Quillix Apps providing a great alternative for small businesses to avoid the large costs and resources required to manage a full Corvane Exchange operation. &nbsp;<a href="#">[More]</a></p>
</article>
<div class="comment abs" style="top:776px">With Corvane making big strides recently to move their huge office suite into the cloud, with Corvane Deskline, this is a great time to revisit the options with Quillix Apps providing a great alternative for small businesses<div class="meta"><a href="#">[ Read More]</a><a href="#">Submited by xxxx</a></div></div>
<div class="comment abs" style="top:847px">With Corvane making big strides recently to move their huge office suite into the cloud, with Corvane Deskline, this is a great time to revisit the options with Quillix Apps providing a great alternative for small businesses<div class="meta"><a href="#">[ Read More]</a><a href="#">Submited by xxxx</a></div></div>
<article class="post abs" style="top:928px">
  <h3>So why cloud software...?</h3>
  <p>Cloud software is a massive area of the market and has emerged as a viable choice for many areas of business in the last year or two. There are however still a lot of misunderstandings and urban myths lurking out there, so we will use this post to hopefully provide some clear information. &nbsp;<a href="#">[More]</a></p>
</article>
<div class="comment abs" style="top:1035px">With Corvane making big strides recently to move their huge office suite into the cloud, with Corvane Deskline, this is a great time to revisit the options with Quillix Apps providing a great alternative for small businesses<div class="meta"><a href="#">[ Read More]</a><a href="#">Submited by xxxx</a></div></div>
<footer class="site-footer abs">
  <div class="footer-links abs">Software Training and Implementation<span class="sep">|</span>Blog<span class="sep">|</span>About Us<span class="sep">|</span>Project Management<span class="sep">|</span>Business Process Analysis<span class="sep">|</span>Contact us</div>
  <div class="copyright abs">Copyright © 2013 Vantrel Media All right reserved. &nbsp;Powered by</div>
  <div class="footer-brand abs">Vantrel Media</div>
</footer>
</body>
</html>
```